Business Card design for a company called Tallow Flame NI

I need a business card design for my oil fired boiler servicing company. I have a logo design already and Im just looking that incorporated into the business card design. card details; Tallow Flame NI
Oil Burner Servicing - Mid Ulster Area
Service Engineer - Owen Marsh
Mobile 07751364927
email - Tallow.Flame.NI@hearthmail.example
www.tallowflameni.example
I carry out Servicing, Commissioning, Fault Finding, Warranty Validation
Target Market(s)
home owners with oil fired central heating
Industry/Entity Type
Business
Contact Information for Business Card
Tallow Flame NI
Tell. 07751364927
Web: www.tallowflameni.example
email Tallow.Flame.NI@Hearthmail.Example
Servicing Fault Finding Commissioning Warranty Validation
Look and feel

```html
<!DOCTYPE html>
<html lang="en">
<head>
<meta charset="utf-8">
<title>Tallow Flame NI – Business Card</title>
<link rel="stylesheet" href="https://fonts.googleapis.com/css2?family=Nunito:wght@700&family=Bodoni+Moda:wght@500&family=Arimo&display=swap">
<style>
  :root {
    --page: #e9e9e9;
    --card: #ffffff;
    --brand-green: #4cba3f;
    --band-light: #a6cf3a;
    --band-dark: #6bbd43;
    --ink: #111111;
    --faint: #d3d3d3;
  }
  * { margin: 0; padding: 0; box-sizing: border-box; }
  html, body { width: 1189px; height: 1200px; overflow: hidden; background: var(--page); }
  .canvas { position: relative; width: 1189px; height: 1200px; }
  .card {
    position: absolute; left: 136px; width: 917px; height: 521px;
    background: var(--card); overflow: hidden;
    box-shadow: 0 4px 10px rgba(0,0,0,.18);
  }
  .card--front { top: 46px; }
  .card--back { top: 624px; }

  .brand-mark {
    position: absolute; border-radius: 50%; background: var(--brand-green);
    width: 190px; height: 190px;
  }
  .brand-name {
    position: absolute; left: 264px;
    font-family: "Nunito", sans-serif; font-weight: 700;
    font-size: 74px; line-height: 1; color: var(--brand-green);
    white-space: nowrap;
  }
  .brand-tagline {
    position: absolute; left: 266px;
    font-family: "Arimo", sans-serif; font-size: 21px; letter-spacing: 3.2px;
    color: var(--brand-green); white-space: nowrap;
  }
  .card--front .brand-mark { left: 49px; top: 40px; }
  .card--front .brand-name { top: 76px; }
  .card--front .brand-tagline { top: 172px; }

  .wave { position: absolute; left: 0; top: 0; width: 100%; height: 100%; }

  .engineer { position: absolute; left: 55px; top: 348px; font-family: "Bodoni Moda", serif; color: var(--ink); }
  .engineer__name { font-size: 48px; line-height: 1; font-weight: 500; }
  .engineer__role { font-size: 26px; line-height: 1.1; font-weight: 500; margin-top: 2px; }

  .divider { position: absolute; left: 415px; top: 315px; width: 2px; height: 148px; background: var(--ink); }

  .contacts { position: absolute; left: 488px; top: 333px; list-style: none;
    font-family: "Arimo", sans-serif; font-size: 22px; color: var(--ink); }
  .contacts li { display: flex; align-items: center; height: 40px; white-space: nowrap; }
  .contacts svg { width: 15px; height: 15px; margin-right: 9px; flex: none; }
  .contacts .email { font-size: 20px; }

  .services {
    position: absolute; left: 0; width: 100%; top: 472px; text-align: center;
    font-family: "Arimo", sans-serif; font-size: 24px; color: var(--ink); white-space: nowrap;
  }

  .backdrop-ring {
    position: absolute; left: 560px; top: 8px; width: 430px; height: 430px;
    border-radius: 50%; border: 36px solid var(--faint); opacity: .8;
  }
  .card--back .brand-mark { left: 46px; top: 147px; }
  .card--back .brand-name { top: 183px; }
  .card--back .brand-tagline { top: 279px; }
</style>
</head>
<body>
<main class="canvas">

  <section class="card card--front" aria-label="Card front">
    <svg class="wave" viewBox="0 0 917 521" preserveAspectRatio="none" aria-hidden="true">
      <defs>
        <linearGradient id="bandGrad" x1="0" y1="0" x2="1" y2="0">
          <stop offset="0" stop-color="var(--band-light)"/>
          <stop offset="1" stop-color="var(--band-dark)"/>
        </linearGradient>
      </defs>
      <path d="M0,260 C220,300 450,280 620,250 C760,225 850,250 917,298 L917,521 L0,521 Z" fill="var(--ink)"/>
      <path d="M0,307 C230,330 470,300 640,268 C770,245 860,270 917,302 L917,521 L0,521 Z" fill="url(#bandGrad)"/>
    </svg>

    <div class="brand-mark" aria-hidden="true"></div>
    <h1 class="brand-name">Tallow Flame NI</h1>
    <p class="brand-tagline">OIL BURNER SERVICING - MID ULSTER AREA</p>

    <div class="engineer">
      <p class="engineer__name">Owen Marsh</p>
      <p class="engineer__role">Service Engineer</p>
    </div>

    <div class="divider" aria-hidden="true"></div>

    <ul class="contacts">
      <li>
        <svg viewBox="0 0 16 16" aria-hidden="true"><rect width="16" height="16" rx="2" fill="var(--ink)"/><path d="M5 3.5l2 2-1 1.2c.6 1.4 1.7 2.5 3.1 3.1l1.2-1 2 2-1.4 1.7C7.5 12 4 8.5 3.5 5z" fill="#fff"/></svg>
        07751364927
      </li>
      <li class="email">
        <svg viewBox="0 0 16 16" aria-hidden="true"><rect y="2" width="16" height="12" rx="1" fill="var(--ink)"/><path d="M2 4.5l6 4.5 6-4.5" fill="none" stroke="#fff" stroke-width="1.3"/></svg>
        Tallow.Flame.NI@Hearthmail.Example
      </li>
      <li>
        <svg viewBox="0 0 16 16" aria-hidden="true"><rect width="16" height="16" rx="2" fill="var(--ink)"/><circle cx="8" cy="8" r="5" fill="none" stroke="#fff" stroke-width="1.3"/><path d="M3 8h10M8 3c-2.5 3-2.5 7 0 10M8 3c2.5 3 2.5 7 0 10" fill="none" stroke="#fff" stroke-width="1"/></svg>
        www.tallowflameni.example
      </li>
    </ul>

    <p class="services">Servicing Fault Finding Commissioning Warranty Validation</p>
  </section>

  <section class="card card--back" aria-label="Card back">
    <div class="backdrop-ring" aria-hidden="true"></div>
    <div class="brand-mark" aria-hidden="true"></div>
    <h2 class="brand-name">Tallow Flame NI</h2>
    <p class="brand-tagline">OIL BURNER SERVICING - MID ULSTER AREA</p>
  </section>

</main>
</body>
</html>
```